Thistlewood Joinery Website

My client Thistlewood Joinery is looking for a redesign for a Word Press Website. Their current site is at www.thistlewoodjoinery.example They are a custom cabinet company, but also create bathroom, living room, bar and entertainment and bedroom cabinets too. They would like a design that emulates the master craftsman work they do yet a contemporary style.

Their current site was designed using Flash elements.

Target Market(s)

Home owners and builders of high end homes

Industry/Entity Type

Entertainment

Font styles to use
Serif
Decorative

Requirements
Must have
• Must show their work and logo using a contemporary style.
Nice to have
• Sliders that showcase their projects.

```html
<!DOCTYPE html>
<html lang="en">
<head>
<meta charset="utf-8">
<title>Thistlewood Joinery</title>
<link href="https://fonts.googleapis.com/css2?family=Josefin+Sans:ital,wght@0,300;0,400;0,600;1,300;1,400&display=swap" rel="stylesheet">
<style>
:root{
  --green:#3cae48;
  --green-dark:#2f8f3a;
  --ink:#222;
  --muted:#6b6458;
  --wood-1:#ede5d7;
  --wood-2:#e3d8c6;
  --black:#0d0d0d;
  --panel:#ffffff;
  --panel-soft:#f5f5f5;
}
*{box-sizing:border-box;margin:0;padding:0}
html,body{width:786px;height:1200px;overflow:hidden}
body{font-family:"Josefin Sans",sans-serif;color:var(--ink);background:linear-gradient(90deg,var(--wood-1),var(--wood-2) 30%,var(--wood-1) 55%,var(--wood-2) 80%,var(--wood-1));position:relative}
.abs{position:absolute}
.topbar{left:0;top:0;width:786px;height:18px;background:var(--black);color:#fff;font-size:8px;display:flex;align-items:center}
.topbar .contact{position:absolute;display:flex;align-items:center;gap:5px}
.topbar .social{position:absolute;right:46px;display:flex;gap:5px}
.topbar .social span{width:8px;height:8px;border-radius:50%;background:#fff;display:block}
.nav{top:67px;height:30px;border-top:1px solid rgba(0,0,0,.08);border-bottom:1px solid rgba(0,0,0,.08);display:flex;align-items:center;justify-content:space-between;font-size:11px;color:#3a3a3a}
.nav .dot{width:3px;height:3px;border-radius:50%;background:#333}
.brand{left:349px;top:25px;width:88px;height:88px;border-radius:50%;background:#fff;border:3px solid #111;display:flex;align-items:center;justify-content:center;text-align:center;font-size:11px;font-weight:600;color:var(--green-dark);line-height:1.2}
.hero{left:0;top:122px;width:786px;height:308px;background:linear-gradient(120deg,#5a2e1c 0%,#8a5a3a 30%,#d9cbb3 55%,#cfc2ad 70%,#f2efe9 100%)}
.caption{left:129px;top:122px;width:208px;height:246px;background:rgba(35,22,15,.86);color:#fff;text-align:center}
.caption h2{font-style:italic;font-weight:300;font-size:14px;margin-top:26px}
.rule{width:90px;height:1px;background:#fff;margin:10px auto}
.caption .thumb{width:160px;height:78px;margin:6px auto 0;background:linear-gradient(135deg,#c08a4a,#e8d4a8)}
.caption p{font-style:italic;font-weight:300;font-size:7.4px;line-height:1.45;padding:12px 18px 0}
.dots{display:flex;gap:10px}
.dots span{width:7px;height:7px;border-radius:50%;background:#fff;border:1px solid #555}
.dots .on{background:var(--green)}
.tile{top:454px;width:136px;height:77px;background:#fff;box-shadow:0 1px 3px rgba(0,0,0,.3)}
.tile b{display:block;height:15px;background:var(--green);color:#fff;font-size:8px;font-weight:600;text-align:center;line-height:16px;letter-spacing:.2px}
.tile i{display:block;height:62px}
.welcome{left:98px;top:552px;width:590px;height:455px;background:var(--panel);box-shadow:0 1px 4px rgba(0,0,0,.35)}
.welcome h1{position:absolute;left:13px;top:23px;font-weight:400;font-size:17px;letter-spacing:.3px}
.welcome .copy{position:absolute;left:13px;top:49px;width:336px;font-size:7.3px;line-height:1.45}
.welcome .copy p+p{margin-top:9px}
.btn{display:inline-block;margin-top:9px;background:var(--green);color:#fff;font-size:7.5px;font-weight:600;padding:3px 5px 2px}
.video{left:362px;top:50px;width:215px;height:120px;background:linear-gradient(160deg,#3b2a1c,#6b4a30 60%,#2a1d14)}
.testimonials{left:0;top:206px;width:590px;height:249px;background:var(--panel-soft);border-top:1px solid #e2e2e2;text-align:center}
.testimonials h3{font-weight:300;font-size:21px;color:var(--green);margin-top:30px;letter-spacing:.5px}
.testimonials blockquote{font-style:italic;font-weight:300;font-size:10px;line-height:1.75;color:#555;width:420px;margin:34px auto 0}
.testimonials cite{display:block;font-size:9.5px;color:#aaa;margin-top:12px}
.arrow{width:32px;height:32px;border-radius:50%;background:#222;top:134px}
.tdots{left:262px;top:226px;display:flex;gap:7px}
.tdots span{width:7px;height:7px;border-radius:50%;background:#c4c4c4}
.tdots .on{background:var(--green);width:10px;height:10px;margin-top:-1px}
.footer-info{left:108px;top:1040px;font-size:7.3px;color:#4a4a4a;line-height:1.9}
.footer-info .row{display:flex;gap:10px;align-items:flex-start}
.icon{width:14px;height:14px;border-radius:50%;background:#fff;display:flex;align-items:center;justify-content:center;flex:none}
.col{top:1040px;font-size:7.3px;color:#4a4a4a;letter-spacing:.3px}
.col h4{font-weight:400;font-size:13px;color:var(--green);margin-bottom:14px;letter-spacing:.5px}
.col li{list-style:none;line-height:15px}
.bottombar{left:0;top:1183px;width:786px;height:17px;background:var(--black);color:#fff;font-size:6px;padding-left:106px;line-height:18px}
</style>
</head>
<body>
<header>
  <div class="abs topbar">
    <span class="contact" style="left:106px"><svg width="9" height="9" viewBox="0 0 24 24"><path fill="#fff" d="M6.6 10.8a15 15 0 006.6 6.6l2.2-2.2c.3-.3.7-.4 1-.2 1.1.4 2.3.6 3.6.6.6 0 1 .4 1 1V20c0 .6-.4 1-1 1A17 17 0 013 4c0-.6.4-1 1-1h3.5c.6 0 1 .4 1 1 0 1.3.2 2.5.6 3.6.1.3 0 .7-.2 1z"/></svg>1-555-010-4477</span>
    <span class="contact" style="left:216px"><svg width="10" height="8" viewBox="0 0 20 14"><rect x="1" y="1" width="18" height="12" fill="none" stroke="#fff" stroke-width="1.6"/><path d="M1 1l9 7 9-7" fill="none" stroke="#fff" stroke-width="1.6"/></svg>sales@thistlewoodjoinery.example</span>
    <span class="social" aria-label="Social links"><span></span><span></span><span></span><span></span></span>
  </div>
  <nav class="abs nav" style="left:100px;width:206px"><span>Cabinets</span><span class="dot"></span><span>Pricing</span><span class="dot"></span><span>About Us</span></nav>
  <div class="abs brand">Thistlewood<br>Joinery</div>
  <nav class="abs nav" style="left:480px;width:206px"><span>Galleries</span><span class="dot"></span><span>Testimonials</span><span class="dot"></span><span>Contact Us</span></nav>
</header>

<section class="abs hero" role="img" aria-label="Kitchen with dark wood cabinets and granite countertops"></section>
<div class="abs caption">
  <h2>Innovative drawer functions</h2>
  <div class="rule"></div>
  <div class="thumb" role="img" aria-label="Pull-out wicker basket drawer"></div>
  <p>Lorem ipsum dolor sit amet, consectetur adipisicing elit, sed do eiusmod tempor incididunt ut labore et dolore magna aliqua. Ut enim ad minim veniam, quis nostrud exercitation ullamco ,</p>
  <div class="rule" style="margin-top:14px"></div>
</div>
<div class="abs dots" style="left:352px;top:411px"><span class="on"></span><span></span><span></span><span></span><span></span></div>

<div class="abs tile" style="left:103px"><b>BROWSE STYLES BY DOOR</b><i role="img" aria-label="White cabinet doors" style="background:linear-gradient(135deg,#d8dde0,#9aa3a8)"></i></div>
<div class="abs tile" style="left:251px"><b>VIEW OUR KITCHEN GALLERY</b><i role="img" aria-label="Bright kitchen interior" style="background:linear-gradient(135deg,#6b5a48,#cfc6b8)"></i></div>
<div class="abs tile" style="left:398px"><b>START YOUR DESIGN</b><i role="img" aria-label="Dark cabinets beside a fridge" style="background:linear-gradient(135deg,#8d8f92,#3a2a20)"></i></div>
<div class="abs tile" style="left:546px"><b>CABINET HARDWARE</b><i role="img" aria-label="Brushed steel cabinet handles" style="background:linear-gradient(135deg,#c9c9c9,#8f8f8f)"></i></div>

<main class="abs welcome">
  <h1>Welcome to Thistlewood Joinery&amp;Fixtures</h1>
  <div class="copy">
    <p>Lorem ipsum dolor sit amet, consectetur adipiscing elit, sed do eiusmod tempor incididunt ut labore et dolore magna aliqua. Ut enim ad minim veniam, quis nostrud exercitation ullamco laboris nisi ut aliquip ex ea commodo consequat. Duis aute irure dolor in reprehenderit in voluptate velit esse cillum dolore eu fugiat nulla pariatur. Excepteur sint occaecat cupidatat non proident, sunt in culpa qui officia deserunt mollit anim id est laborum.</p>
    <p>Lorem ipsum dolor sit amet, consectetur adipiscing elit, sed do eiusmod tempor incididunt ut labore et dolore magna aliqua. Ut enim ad minim veniam, quis nostrud exercitation ullamco laboris nisi ut aliquip ex ea commodo consequat.</p>
    <span class="btn">READ MORE</span>
  </div>
  <div class="abs video" role="img" aria-label="Video of founder Walter Greer in a cabinet showroom"></div>
  <section class="abs testimonials">
    <h3>TESTIMONIALS</h3>
    <svg class="abs" style="left:286px;top:66px" width="20" height="16" viewBox="0 0 20 16"><path fill="#cfcfcf" d="M0 16V9C0 4 2 1 7 0v3C5 4 4 6 4 8h4v8zm11 0V9c0-5 2-8 7-9v3c-2 1-3 3-3 5h4v8z"/></svg>
    <blockquote>Lorem ipsum dolor sit amet, consectetur adipisicing elit, sed do eiusmod tempor incididunt ut labore et dolore magna aliqua. Ut enim ad minim veniam, quis nostrud exercitation ullamco laboris nisi ut aliquip ex ea commodo consequat.<cite>- Marcus &amp; Elena, CA</cite></blockquote>
    <div class="abs arrow" style="left:15px"><svg width="32" height="32"><path d="M18 11l-5 5 5 5" stroke="#fff" stroke-width="2" fill="none"/></svg></div>
    <div class="abs arrow" style="left:542px"><svg width="32" height="32"><path d="M14 11l5 5-5 5" stroke="#fff" stroke-width="2" fill="none"/></svg></div>
    <div class="abs tdots"><span class="on"></span><span></span><span></span><span></span><span></span><span></span></div>
  </section>
</main>

<footer>
  <div class="abs footer-info">
    <div class="row"><span class="icon"><svg width="8" height="10" viewBox="0 0 12 16"><path fill="#3cae48" d="M6 0a6 6 0 00-6 6c0 4.5 6 10 6 10s6-5.5 6-10a6 6 0 00-6-6zm0 8.5A2.5 2.5 0 116 3.5a2.5 2.5 0 010 5z"/></svg></span><span style="line-height:1.85">Thistlewood Joinery<br>4820 Elm Hollow Rd<br>Fairview, TX, USA 75069</span></div>
    <div class="row" style="margin-top:10px"><span class="icon"><svg width="8" height="8" viewBox="0 0 24 24"><path fill="#3cae48" d="M6.6 10.8a15 15 0 006.6 6.6l2.2-2.2c.3-.3.7-.4 1-.2 1.1.4 2.3.6 3.6.6.6 0 1 .4 1 1V20c0 .6-.4 1-1 1A17 17 0 013 4c0-.6.4-1 1-1h3.5c.6 0 1 .4 1 1 0 1.3.2 2.5.6 3.6.1.3 0 .7-.2 1z"/></svg></span>Phone: 1-555-010-4477</div>
    <div class="row" style="margin-top:10px"><span class="icon"><svg width="8" height="6" viewBox="0 0 20 14"><rect x="1" y="1" width="18" height="12" fill="none" stroke="#3cae48" stroke-width="2"/><path d="M1 1l9 7 9-7" fill="none" stroke="#3cae48" stroke-width="2"/></svg></span>sales@thistlewoodjoinery.example</div>
    <div class="row" style="margin-top:10px"><span class="icon"><svg width="9" height="9" viewBox="0 0 20 20"><circle cx="10" cy="10" r="8" fill="none" stroke="#3cae48" stroke-width="2"/><path d="M10 5v5l3 2" stroke="#3cae48" stroke-width="2" fill="none"/></svg></span>Monday - Friday -8:00 - 5:00</div>
  </div>
  <div class="abs col" style="left:281px"><h4>Get Started</h4><ul><li>Find Your Style</li><li>Design Your Room</li><li>Plan Your Project</li><li>Install Your Cabinets</li><li>Love Your Space</li></ul></div>
  <div class="abs col" style="left:415px"><h4>About Us</h4><ul><li>About Thistlewood Joinery</li><li>What We Stand For</li><li>Our Brand Portfolio</li><li>Our Dealer Network</li><li>Committed to Sustainability</li></ul></div>
  <div class="abs col" style="left:573px"><h4>Assistance</h4><ul><li>Sitemap</li><li>Privacy Policy</li><li>Legal</li><li>Careers</li><li>News</li></ul></div>
  <div class="abs bottombar">©2015 Thistlewoodjoinery.example. ALL RIGHTS RESERVED.</div>
</footer>
</body>
</html>
```